Business Card Design Project

Corwen Property Management

Our Business is residential property management, we therefore need a card that displays a professional image, but is clear and concise, and easy to read
Updates

We are committed now guys and girls, loving what we are seeing so far! 

Target Market(s)

Landlords, Rental Property Owners

Industry/Entity Type

Residential

Requirements
Must have
• Dean Fosterly - Principal
Tessa Fosterly - Director (Property Management)

PO Box 718
Holloway SA 5093

Dean: 0419 372 508
Tessa: 0419 613 947

www.corwenpropertymanagement.com.au
admin@corwenpropertymanagement.com.au

Nice to have
• I would like the card to be double sided, white background on the information side and then colour on the reverse, in blue or black and incorporating our logo

```html
<!DOCTYPE html>
<html lang="en">
<head>
<meta charset="utf-8">
<title>Corwen Property Management – Business Card</title>
<link rel="stylesheet" href="https://fonts.googleapis.com/css2?family=Lato:wght@400;700&display=swap">
<style>
  :root {
    --page-bg: #e6eaec;
    --card-white: #ffffff;
    --brand-blue: #1a6fc0;
    --brand-blue-light: #2d8fdc;
    --brand-blue-dark: #0f56a0;
    --text-grey: #4a4a4a;
    --text-dark: #333333;
    --rule-blue: #2a86d1;
  }
  * { box-sizing: border-box; margin: 0; padding: 0; }
  html, body {
    width: 1200px;
    height: 960px;
    overflow: hidden;
    background: var(--page-bg);
    font-family: "Lato", Arial, sans-serif;
  }
  .canvas {
    position: relative;
    width: 1200px;
    height: 960px;
  }
  .card {
    position: absolute;
    left: 290px;
    width: 620px;
    height: 380px;
    box-shadow: 0 6px 18px rgba(0, 0, 0, 0.18);
  }
  .card--front {
    top: 70px;
    background: var(--card-white);
    color: var(--text-grey);
    padding: 40px 34px 0 36px;
  }
  .card--back {
    top: 500px;
    background: radial-gradient(ellipse at 50% 40%, var(--brand-blue-light) 0%, var(--brand-blue) 55%, var(--brand-blue-dark) 100%);
    display: flex;
    align-items: center;
    justify-content: center;
  }

  .brand {
    display: flex;
    align-items: center;
    gap: 14px;
    white-space: nowrap;
  }
  .brand__mark {
    width: 46px;
    height: 46px;
    background: var(--brand-blue);
    flex: none;
  }
  .brand__name {
    font-size: 30px;
    font-weight: 700;
    color: var(--text-grey);
    letter-spacing: 0.2px;
  }
  .card--back .brand__mark { background: var(--card-white); }
  .card--back .brand__name { color: var(--card-white); font-size: 34px; }

  .people {
    margin-top: 54px;
  }
  .person {
    display: flex;
    align-items: baseline;
    gap: 7px;
    white-space: nowrap;
    font-size: 14px;
    color: var(--text-grey);
    padding: 6px 0;
  }
  .person__name {
    flex: none;
    font-size: 22px;
    text-transform: uppercase;
    color: var(--text-grey);
    letter-spacing: 0.2px;
  }
  .person__detail {
    flex: none;
  }
  .people__rule {
    height: 2px;
    background: var(--rule-blue);
    margin: 4px 0;
  }

  .contact {
    margin-top: 24px;
    font-size: 17px;
    line-height: 1.5;
    color: var(--text-grey);
    white-space: nowrap;
  }
  .contact__web {
    font-weight: 700;
    color: var(--text-dark);
  }
</style>
</head>
<body>
<main class="canvas">
  <section class="card card--front" aria-label="Card front">
    <div class="brand">
      <span class="brand__mark"></span>
      <span class="brand__name">Corwen Property Management</span>
    </div>

    <div class="people">
      <p class="person">
        <span class="person__name">Dean Fosterly</span>
        <span class="person__detail">| Principal | T: 0419 372 508</span>
      </p>
      <div class="people__rule"></div>
      <p class="person">
        <span class="person__name">Tessa Fosterly</span>
        <span class="person__detail">| Director (Property Management) | T: 0419 613 947</span>
      </p>
    </div>

    <div class="contact">
      <p>E: admin@corwenpropertymanagement.com.au</p>
      <p>PO Box 718, Holloway SA 5093</p>
      <p class="contact__web">www.corwenpropertymanagement.com.au</p>
    </div>
  </section>

  <section class="card card--back" aria-label="Card back">
    <div class="brand">
      <span class="brand__mark"></span>
      <span class="brand__name">Corwen Property Management</span>
    </div>
  </section>
</main>
</body>
</html>
```